Willow Creek Haven website design

To create 2 pages (a front page and sub page) for a health/spiritual website. I have a logo, and was thinking of incorporating Greek temple columns in the design or something similar, but open to other ideas.

The design should suit mobile devices with limited screen space also.

Industry/Entity Type

Health

Number of Pages Required

1 page

```html
<!DOCTYPE html>
<html lang="en">
<head>
<meta charset="utf-8">
<title>Willow Creek Haven</title>
<link rel="stylesheet" href="https://fonts.googleapis.com/css2?family=Cinzel:wght@400;700&family=Open+Sans:wght@400;600;700&family=Great+Vibes&display=swap">
<style>
:root{
  --ink:#1b1b1b;
  --night:#171717;
  --white:#fff;
  --muted:#4a4a4a;
}
*{box-sizing:border-box;margin:0;padding:0}
html,body{width:1200px;height:2643px;overflow:hidden}
body{position:relative;background:var(--white);color:var(--ink);font-family:"Open Sans",Arial,sans-serif}
a{color:inherit;text-decoration:none}
.abs{position:absolute}

/* header */
.site-header{position:absolute;left:0;top:0;width:1200px;height:176px;background:linear-gradient(#1e1e1e,#121212);color:var(--white)}
.brand{left:99px;top:62px;width:170px;text-align:center;font-family:"Cinzel",serif;font-size:19px;line-height:1.25;color:var(--white)}
.call{left:636px;top:38px;display:flex;align-items:center;gap:10px;font-size:17px;font-weight:600}
.icon-ring{width:32px;height:32px;border:2px solid var(--white);border-radius:50%;display:inline-flex;align-items:center;justify-content:center}
.social{display:flex;gap:6px}
.social span{width:33px;height:33px;border:2px solid var(--white);border-radius:50%;display:block}
.header-social{left:909px;top:36px}
.main-nav{left:380px;top:106px;display:flex;font-size:19px;font-weight:600}
.main-nav a{margin-right:50px}
.main-nav a:last-child{margin-right:0}
.dropdown{left:472px;top:159px;width:201px;height:186px;background:#141414;border-top:3px solid var(--white);z-index:5;padding:26px 0 0 22px;color:var(--white);font-size:15px}
.dropdown::before{content:"";position:absolute;left:30px;top:-12px;border:9px solid transparent;border-bottom-color:var(--white);border-top:0}
.dropdown li{list-style:none;display:flex;align-items:center;gap:14px;height:36px}
.dropdown li::before{content:"";width:12px;height:12px;border-radius:50%;background:var(--white)}

/* hero */
.hero-photo{left:0;top:176px;width:1200px;height:479px;background:linear-gradient(100deg,#aebfcf 0%,#c8cfd3 30%,#c99a55 55%,#8a6434 80%,#d1a465 100%)}
.hero-title{left:98px;top:248px;font-family:"Cinzel",serif;font-weight:700;font-size:40px;line-height:54px;color:var(--ink)}
.btn-outline{display:inline-flex;align-items:center;justify-content:center;border:2px solid var(--ink);font-size:14px;font-weight:600;text-transform:uppercase}
.hero-btn{left:98px;top:377px;width:122px;height:46px}
.hero-arrows{left:98px;top:450px}

.promo-band{left:0;top:655px;width:1200px;height:85px;background:var(--night);color:var(--white)}
.promo-script{left:100px;top:20px;font-family:"Great Vibes",cursive;font-size:38px}
.promo-text{left:440px;top:32px;font-size:14px}
.promo-btn{left:932px;top:22px;width:170px;height:41px;border:2px solid var(--white);color:var(--white);font-weight:700;font-size:15px}

/* headings */
.section-title{position:absolute;left:0;width:1200px;display:flex;justify-content:center;align-items:center;gap:24px;font-family:"Cinzel",serif;font-weight:700;font-size:31px;color:var(--ink)}
.flourish{width:50px;height:3px;background:var(--ink);border-radius:2px}
.lead{position:absolute;left:150px;width:900px;text-align:center;font-size:14px;line-height:25px;color:var(--muted)}

/* feature circles */
.feature{position:absolute;top:955px;width:282px;height:282px;border-radius:50%;color:var(--white);text-align:center}
.feature h3{margin-top:88px;font-size:20px;font-weight:600;text-transform:uppercase;letter-spacing:-.3px}
.feature .rule{width:110px;height:2px;background:var(--white);margin:22px auto 30px}
.feature .btn{display:inline-block;border:2px solid var(--white);padding:7px 14px;font-size:15px;background:rgba(0,0,0,.3)}
.f1{left:116px;background:radial-gradient(circle at 40% 60%,#d2884a,#5a2c1c 75%)}
.f2{left:460px;background:radial-gradient(circle at 60% 50%,#6b4a3a,#3a0d12 75%)}
.f3{left:802px;background:radial-gradient(circle at 50% 50%,#bdaeb2,#5e3f3f 80%)}

/* spiritual band */
.spirit{left:0;top:1309px;width:1200px;height:494px;background:radial-gradient(ellipse at 50% 40%,#4b3f2c,#231c14 75%);color:var(--white)}
.spirit-kicker{left:0;width:1200px;top:50px;text-align:center;font-size:22px;font-weight:600;text-transform:uppercase}
.spirit-title{left:0;width:1200px;top:93px;text-align:center;font-family:"Cinzel",serif;font-weight:700;font-size:37px}
.spirit-ring{left:509px;top:167px;width:184px;height:184px;border:2px solid var(--white);border-radius:50%}
.spirit-text{font-size:14px;line-height:23px}
.st-left{left:97px;top:224px;width:376px;text-align:right}
.st-right{left:727px;top:224px;width:376px}
.st-bottom{left:418px;top:381px;width:366px;text-align:center}

/* steps */
.step{position:absolute;top:2008px;width:292px;height:155px;border:2px solid var(--ink);border-radius:50%;display:flex;align-items:center;padding-left:34px}
.step .num{font-size:44px;margin-right:16px}
.step h4{font-size:17px;font-weight:700;margin-bottom:8px}
.step p{font-size:13px;line-height:20px;color:var(--muted)}
.s1{left:97px}.s2{left:453px}.s3{left:807px}
.step-arrow{position:absolute;top:2073px}

/* footer */
.site-footer{position:absolute;left:0;top:2225px;width:1200px;height:418px;background:linear-gradient(#1d1d1d,#141414);color:var(--white)}
.footer-brand{left:100px;top:170px;width:220px;text-align:center;font-family:"Cinzel",serif;font-size:21px}
.f-col-title{font-size:17px;font-weight:700;text-transform:uppercase;padding-bottom:12px;border-bottom:2px solid var(--white);display:inline-block}
.quick{left:400px;top:63px}
.quick li{list-style:none;font-size:15px;margin-top:13px}
.quick li::before{content:"› "}
.contact{left:578px;top:63px;font-size:13px;line-height:20px}
.contact-row{display:flex;gap:18px;margin-top:20px}
.contact-row b{font-size:14px}
.contact-icon{width:40px;height:40px;flex:none}
.form{left:848px;top:63px;width:254px;height:220px}
.field{position:absolute;border:1px solid var(--white);border-radius:4px;font-size:12px;padding:6px 10px}
.send{position:absolute;left:0;top:177px;width:118px;height:38px;background:var(--white);color:var(--ink);font-size:13px;font-weight:600;display:flex;align-items:center;justify-content:center;border-radius:3px}
.footer-rule{left:98px;top:344px;width:1004px;height:1px;background:#888}
.copyright{left:98px;top:370px;font-size:14px;font-weight:700}
.footer-social{left:947px;top:360px}
</style>
</head>
<body>

<header class="site-header">
  <div class="abs brand">Willow Creek Haven</div>
  <div class="abs call">
    <span class="icon-ring"><svg width="16" height="16" viewBox="0 0 24 24"><path fill="#fff" d="M6.6 10.8a15 15 0 0 0 6.6 6.6l2.2-2.2c.3-.3.7-.4 1-.2 1.1.4 2.3.6 3.6.6.6 0 1 .4 1 1V20c0 .6-.4 1-1 1A17 17 0 0 1 3 4c0-.6.4-1 1-1h3.5c.6 0 1 .4 1 1 0 1.3.2 2.5.6 3.6.1.3 0 .7-.2 1z"/></svg></span>
    CALL US AT: 180 555 0147
  </div>
  <div class="abs social header-social"><span></span><span></span><span></span><span></span><span></span></div>
  <nav class="abs main-nav">
    <a href="#">Home</a><a href="#">About</a><a href="#">Greek Temples</a><a href="#">Gallery</a><a href="#">News &amp; Blog</a><a href="#">Contacts</a>
  </nav>
</header>

<ul class="abs dropdown">
  <li>History</li><li>Team</li><li>FAQs</li><li>Greek Temples</li>
</ul>

<div class="abs hero-photo" role="img" aria-label="Photograph of ancient Greek temple columns under a pale sky"></div>
<h1 class="abs hero-title">Willow Creek<br>Haven</h1>
<a class="abs btn-outline hero-btn" href="#">Read More</a>
<svg class="abs hero-arrows" width="80" height="44" viewBox="0 0 80 44"><path d="M20 2 2 22l18 20M50 2l18 20-18 20" fill="none" stroke="#1b1b1b" stroke-width="2"/></svg>

<section class="abs promo-band">
  <div class="abs promo-script">Read about All Temples:</div>
  <p class="abs promo-text">Ut wisi enim ad minim veniam, est etiam processus dynamiquis nostrud</p>
  <a class="abs btn-outline promo-btn" href="#">Read More</a>
</section>

<h2 class="section-title" style="top:796px"><span class="flourish"></span>Welcome To Willow Creek Haven<span class="flourish"></span></h2>
<p class="lead" style="top:857px">Sed ut perspiciatis unde omnis iste natus error sit voluptatem accusantium doloremque laudantium, totam rem aperiam, eaque ipsa quae ab illo inventore veritatis et quasi architecto beatae vitae dicta sunt explicabo.</p>

<div class="feature f1" role="img" aria-label="Photograph of a temple at sunset">
  <h3>Greek Temples</h3><div class="rule"></div><a class="btn" href="#">Read More</a>
</div>
<div class="feature f2" role="img" aria-label="Photograph of a candlelit temple interior">
  <h3>Health &amp; Spiritual</h3><div class="rule"></div><a class="btn" href="#">Read More</a>
</div>
<div class="feature f3" role="img" aria-label="Photograph of a pale stone colonnade">
  <h3>Greek Temples</h3><div class="rule"></div><a class="btn" href="#">Read More</a>
</div>

<section class="abs spirit" role="img" aria-label="Photograph of temple ruins at dusk">
  <div class="abs spirit-kicker">Health &amp; Spiritual</div>
  <h2 class="abs spirit-title">Willow Creek Haven</h2>
  <div class="abs spirit-ring"></div>
  <p class="abs spirit-text st-left">Nemo enim ipsam voluptatem quia voluptas sit aspernatur aut odit aut fugit, sed quia consequuntur magni dolores eos qui ratione voluptatem</p>
  <p class="abs spirit-text st-right">Nemo enim ipsam voluptatem quia voluptas sit asperna ur aut odit aut fugit, sed quia consequuntur magni dolores eos qui ratione voluptatem</p>
  <p class="abs spirit-text st-bottom">Nemo enim ipsam voluptatem quia voluptas sit asperna ur aut odit aut fugit, sed quia consequuntur magni dolores eos qui ratione voluptatem</p>
</section>

<h2 class="section-title" style="top:1840px"><span class="flourish"></span>To See Our Temples You Must<span class="flourish"></span></h2>
<p class="lead" style="top:1901px">Sed ut perspiciatis unde omnis iste natus error sit voluptatem accusantium doloremque laudantium, totam rem aperiam, eaque ipsa quae ab illo inventore veritatis et quasi architecto beatae vitae dicta sunt explicabo.</p>

<div class="step s1"><span class="num">1.</span><div><h4>NON HABENT</h4><p>Duis autem vel eum iriure<br>dolor in hendrerit in vulp</p></div></div>
<svg class="step-arrow" style="left:399px" width="42" height="26" viewBox="0 0 42 26"><path d="M1 8h26V2l13 11-13 11v-6H1z" fill="none" stroke="#1b1b1b" stroke-width="2"/></svg>
<div class="step s2"><span class="num">2.</span><div><h4>IRIRNUARE</h4><p>Duis autem vel eum iriure<br>dolor in hendrerit in vulp</p></div></div>
<svg class="step-arrow" style="left:757px" width="42" height="26" viewBox="0 0 42 26"><path d="M1 8h26V2l13 11-13 11v-6H1z" fill="none" stroke="#1b1b1b" stroke-width="2"/></svg>
<div class="step s3"><span class="num">3.</span><div><h4>BENT DOLOR</h4><p>Duis autem vel eum iriure<br>dolor in hendrerit in vulp</p></div></div>

<footer class="site-footer">
  <div class="abs footer-brand">Willow Creek Haven</div>

  <div class="abs quick">
    <div class="f-col-title">Quick Links</div>
    <ul><li>Home</li><li>About Us</li><li>Greek Temples</li><li>Gallery</li><li>News &amp; Blog</li><li>Contact Us</li></ul>
  </div>

  <div class="abs contact">
    <div class="f-col-title">Contact Us</div>
    <div class="contact-row"><span class="icon-ring contact-icon"><svg width="16" height="18" viewBox="0 0 24 24"><path fill="none" stroke="#fff" stroke-width="2" d="M12 22s7-7 7-12a7 7 0 0 0-14 0c0 5 7 12 7 12z"/><circle cx="12" cy="10" r="2.5" fill="#fff"/></svg></span><div><b>ADVANCE OFFICE</b><br>42 Linden Row, Fairbrook,<br>NC. (555) 310-2288</div></div>
    <div class="contact-row" style="align-items:center"><span class="icon-ring contact-icon"><svg width="16" height="16" viewBox="0 0 24 24"><path fill="#fff" d="M6.6 10.8a15 15 0 0 0 6.6 6.6l2.2-2.2c.3-.3.7-.4 1-.2 1.1.4 2.3.6 3.6.6.6 0 1 .4 1 1V20c0 .6-.4 1-1 1A17 17 0 0 1 3 4c0-.6.4-1 1-1h3.5c.6 0 1 .4 1 1 0 1.3.2 2.5.6 3.6.1.3 0 .7-.2 1z"/></svg></span><div><b>PHONE:</b> 180 555 0147</div></div>
    <div class="contact-row"><span class="icon-ring contact-icon"><svg width="18" height="14" viewBox="0 0 24 18"><rect x="1" y="1" width="22" height="16" fill="none" stroke="#fff" stroke-width="2"/><path d="M1 2l11 8 11-8" fill="none" stroke="#fff" stroke-width="2"/></svg></span><div><b>MAIL:</b> info@willowcreek<br>haven.in</div></div>
  </div>

  <div class="abs form">
    <div class="f-col-title">Contact Form</div>
    <div class="field" style="left:0;top:52px;width:122px;height:35px">Name</div>
    <div class="field" style="left:130px;top:52px;width:124px;height:35px">Phone</div>
    <div class="field" style="left:0;top:96px;width:254px;height:65px">Address</div>
    <div class="send">SEND MESSAGE</div>
  </div>

  <div class="abs footer-rule"></div>
  <p class="abs copyright">Copyright © 2016 Willow Creek Haven. All Right Reserved</p>
  <div class="abs social footer-social"><span></span><span></span><span></span><span></span></div>
</footer>

</body>
</html>
```